Take my logo and make me some cool looking business cards

I've got a logo that we've trademarked so you can't change the logo but you can change it's color combo and find a fun way to incorporate it into a new business card design that is fresh, stylish, and can be applied to some cool medium cost materials (plastic, wood, metal, etc). Basically, we're looking for business cards that stand out in a good way.
Updates
Here's the logo we're currently using:
Thanks to everyone that has submitted designs. We've narrowed down to the top 4 designs and tried to eliminate old versions or designs that just didn't match our vision as quickly as we could. We don't plan on keeping this open for the full 9 days; we plan on selecting a design in the next 48 hours; with the goal of having something in the hands of a printer, preferably plastic printer, by Thursday AM Pacific Time.
Industry/Entity Type
Business
Requirements
Must have
- must include our existing logo

```html
<!DOCTYPE html>
<html lang="en">
<head>
<meta charset="utf-8">
<title>Kestrel Business Cards</title>
<link rel="stylesheet" href="https://fonts.googleapis.com/css2?family=Open+Sans:ital,wght@0,400;0,600;0,700;1,400&display=swap">
<style>
  :root {
    --page: #d9d6da;
    --blue-deep: #1557a8;
    --blue: #1f6fc0;
    --blue-light: #3a8fd6;
    --white: #ffffff;
    --ink: #1a1a1a;
    --plastic-a: #c94f2a;
    --plastic-b: #e0b52a;
    --wood-a: #a8702c;
    --wood-b: #d9a55a;
    --metal-a: #b8bcc2;
    --metal-b: #eef0f2;
  }
  * { box-sizing: border-box; margin: 0; padding: 0; }
  html, body { width: 1200px; height: 999px; overflow: hidden; }
  body {
    background: var(--page);
    font-family: "Open Sans", Arial, sans-serif;
    position: relative;
  }
  .card {
    position: absolute;
    width: 520px;
    height: 297px;
    overflow: hidden;
    background: radial-gradient(ellipse at 60% 40%, var(--blue-light) 0%, var(--blue) 45%, var(--blue-deep) 100%);
    box-shadow: 0 10px 28px rgba(0,0,0,.25);
  }
  .card--back { left: 50px; top: 351px; }
  .card--front { left: 630px; top: 351px; }

  /* back side */
  .band {
    position: absolute; left: 0; width: 100%;
    background: var(--white);
  }
  .card--back .band { top: 118px; height: 118px; }
  .rule { position: absolute; left: 0; width: 100%; height: 3px; background: var(--blue); }
  .card--back .rule--a { top: 128px; }
  .card--back .rule--b { top: 224px; }
  .material {
    position: absolute; width: 128px; height: 118px;
    border: 3px solid var(--white);
  }
  .material--plastic { left: 40px; top: 20px; background: linear-gradient(135deg, var(--plastic-a), #4c5fb0 45%, var(--plastic-b)); }
  .material--wood { left: 184px; top: 64px; background: linear-gradient(160deg, var(--wood-b), var(--wood-a)); }
  .material--metal { left: 328px; top: 108px; background: linear-gradient(135deg, var(--metal-b), var(--metal-a)); }
  .material-label {
    position: absolute; color: var(--blue-deep); font-weight: 700; font-size: 21px; letter-spacing: .5px;
  }
  .label--plastic { left: 52px; top: 140px; }
  .label--wood { left: 214px; top: 184px; }
  .label--metal { left: 356px; top: 230px; color: var(--white); }

  /* front side */
  .brand {
    position: absolute; right: 40px; top: 42px;
    display: flex; align-items: center; gap: 12px;
    color: var(--white); font-size: 58px; font-weight: 600; letter-spacing: 2px;
  }
  .brand-dot { width: 22px; height: 22px; border-radius: 50%; background: var(--white); }
  .card--front .band { top: 140px; height: 94px; }
  .card--front .rule--a { top: 228px; }
  .card--front .rule--b { top: 270px; background: var(--white); }
  .person { position: absolute; left: 26px; top: 150px; }
  .person-name { color: var(--blue); font-weight: 700; font-size: 22px; line-height: 1.1; }
  .person-role { color: var(--ink); font-size: 12px; }
  .contact { position: absolute; font-size: 11px; color: var(--ink); line-height: 1.7; }
  .contact--phone { left: 200px; top: 190px; }
  .contact--web { left: 350px; top: 190px; }
  .contact div { display: flex; align-items: center; gap: 6px; }
  .contact svg { width: 11px; height: 11px; fill: var(--blue-deep); }
  .address {
    position: absolute; left: 0; width: 100%; top: 238px; text-align: center;
    color: var(--white); font-style: italic; font-size: 15px;
  }
</style>
</head>
<body>

<section class="card card--back" aria-label="Card back">
  <div class="band"></div>
  <div class="rule rule--a"></div>
  <div class="rule rule--b"></div>
  <div class="material material--plastic" role="img" aria-label="Photo of colourful interlocking plastic tiles"></div>
  <div class="material material--wood" role="img" aria-label="Photo of wooden planks"></div>
  <div class="material material--metal" role="img" aria-label="Photo of diamond plate metal"></div>
  <span class="material-label label--plastic">PLASTIC</span>
  <span class="material-label label--wood">WOOD</span>
  <span class="material-label label--metal">METAL</span>
</section>

<section class="card card--front" aria-label="Card front">
  <div class="brand"><span class="brand-dot"></span><span>KESTREL</span></div>
  <div class="band"></div>
  <div class="rule rule--a"></div>
  <div class="rule rule--b"></div>
  <div class="person">
    <div class="person-name">Your Name</div>
    <div class="person-role">designation</div>
  </div>
  <div class="contact contact--phone">
    <div><svg viewBox="0 0 24 24"><path d="M6.6 10.8a15 15 0 0 0 6.6 6.6l2.2-2.2c.3-.3.7-.4 1-.2 1.1.4 2.3.6 3.6.6.6 0 1 .4 1 1V20c0 .6-.4 1-1 1A17 17 0 0 1 3 4c0-.6.4-1 1-1h3.5c.6 0 1 .4 1 1 0 1.3.2 2.5.6 3.6.1.3 0 .7-.2 1z"/></svg>: 123 4564 7899</div>
    <div><svg viewBox="0 0 24 24"><path d="M4 8h16v11H4zM7 3h10v4H7zm2 8h2v2H9zm4 0h2v2h-2zm-4 4h2v2H9zm4 0h2v2h-2z"/></svg>: 123 4564 7899</div>
  </div>
  <div class="contact contact--web">
    <div><svg viewBox="0 0 24 24"><path d="M2 5h20v14H2zm2 2v.5l8 5 8-5V7z"/></svg>: kestrel@mailbox.com</div>
    <div><svg viewBox="0 0 24 24"><circle cx="12" cy="12" r="10"/></svg>: kestrel.com</div>
  </div>
  <div class="address">Address here, address here, address here, address here</div>
</section>

</body>
</html>
```